A4 fitness centre email specials brochure

Quorel Signal Works have been providing audio visual services and support to fitness centres and health clubs for more than 10 years. We are seen as the "to-go" company for anything to do with Audio visual equipment yet we do not produce marketing material or promotional material for these customers so this is our first attempt at promotion. We wish to produce a PDF brochure suitable for emailing to existing and new clients promoting our products and services with special offers using the text contact on the attached draft. The brochure is simple but should carry the company logo in a prominant position, our corporate blue colour, and be easily read. a good photo can be used as a shaded backgound.

Target Market(s)

Health Club managers, fitness instructors

Industry/Entity Type

Fitness Equipment

Font styles to use
Sans Serif

Colors
0455a3

Requirements
Must have
• our corporate colour (blue) a good tag headline (Eg- AV fitness specials) and be easy to read. The brochure will be used as a PDF flyer to attach to emails and may also be printed to mail in some cased
Nice to have
• a picture of a gym with AV equipment in the background, maybe as a water mark image or faded. The brochure should reflect the fitness industry in order to grasp attention to our audience If space allows, maybe just have our offices mentioned in the contact details such as.... Melbourne-Brisbane-Sydney-Perth
Should not have
• don't want it to look cheap - we are the market leader for this sector for over 10 years and it should look professional

```html
<!DOCTYPE html>
<html lang="en">
<head>
<meta charset="utf-8">
<title>Quorel Signal Works – Fitness Specials</title>
<link href="https://fonts.googleapis.com/css2?family=Montserrat:wght@400;500;600;700&family=Oswald:wght@500;600&family=Raleway:wght@400&display=swap" rel="stylesheet">
<style>
  :root {
    --stage: #e3e3e3;
    --paper: #ffffff;
    --ink: #1d1d1f;
    --teal: #1291b9;
    --gold: #fcc431;
    --shape: #ececec;
    --shape-soft: #f4f4f4;
    --speaker: #2e2d31;
    --speaker-light: #5a595e;
    --chrome: #b9babd;
    --rack: #1c1c1f;
    --mixer-tone: #3b332a;
    --accent-orange: #e07b2a;
  }
  * { box-sizing: border-box; margin: 0; padding: 0; }
  html, body { width: 1200px; height: 900px; overflow: hidden; }
  body {
    background: var(--stage);
    font-family: "Montserrat", sans-serif;
    color: var(--ink);
    position: relative;
  }
  .page {
    position: absolute;
    top: 50px;
    width: 540px;
    height: 698px;
    background: var(--paper);
    box-shadow: 3px 4px 6px rgba(0,0,0,0.28);
    overflow: hidden;
  }
  .page--plain { left: 52px; }
  .page--photo { left: 613px; }
  .abs { position: absolute; }
  .decor, .connectors { position: absolute; left: 0; top: 0; width: 540px; height: 698px; }
  .backdrop-photo {
    left: 0; top: 170px; width: 540px; height: 528px;
    background:
      radial-gradient(ellipse 45% 40% at 14% 42%, rgba(160,160,160,0.55), rgba(200,200,200,0) 70%),
      radial-gradient(ellipse 50% 45% at 85% 80%, rgba(175,175,175,0.5), rgba(210,210,210,0) 70%),
      linear-gradient(180deg, rgba(255,255,255,0) 0%, rgba(205,205,205,0.55) 30%, rgba(215,215,215,0.6) 100%);
  }
  .brand { left: 27px; top: 29px; display: flex; align-items: center; gap: 10px; }
  .brand-mark { width: 34px; height: 26px; background: var(--teal); }
  .brand-name { font-size: 15px; font-weight: 500; color: #2a2a2a; letter-spacing: -0.1px; }
  .tagline { right: 30px; top: 36px; font-size: 11px; font-weight: 600; color: var(--teal); }
  .headline { left: 36px; top: 96px; font-size: 14.5px; font-weight: 700; letter-spacing: 0.2px; text-transform: uppercase; }
  .intro { left: 36px; top: 130px; width: 480px; font-size: 9.6px; line-height: 1.3; }

  /* product photo areas */
  .speaker {
    top: 182px; width: 80px; height: 120px; border-radius: 14px 14px 6px 6px;
    background:
      radial-gradient(circle at 50% 68%, #1a1a1c 0 26%, var(--speaker-light) 30%, var(--speaker) 42%),
      var(--speaker);
  }
  .speaker--left { left: 46px; }
  .speaker--right { left: 135px; }
  .product--amp {
    left: 248px; top: 190px; width: 245px; height: 47px; border-radius: 2px;
    background: linear-gradient(180deg, var(--chrome) 0 8%, #2a2a2d 14%, #3b3b3f 50%, #1e1e21 100%);
  }
  .product--player {
    left: 248px; top: 305px; width: 245px; height: 48px; border-radius: 2px;
    background:
      radial-gradient(circle at 55% 50%, #4c4c52 0 12%, transparent 14%),
      linear-gradient(180deg, #2f2f33, var(--rack));
  }
  .product--mixer {
    left: 248px; top: 363px; width: 245px; height: 33px; border-radius: 2px;
    background: linear-gradient(90deg, var(--mixer-tone), #26231f 30%, #2a2926 100%);
  }
  .label {
    background: var(--teal);
    color: #fff;
    font-size: 10.5px;
    font-weight: 600;
    text-align: center;
    line-height: 1.25;
    display: flex; align-items: center; justify-content: center;
  }
  .label--speakers { left: 45px; top: 305px; width: 170px; height: 49px; }
  .label--amp { left: 248px; top: 242px; width: 245px; height: 50px; }
  .label--mixer { left: 248px; top: 401px; width: 245px; height: 49px; }
  .offer-lead { left: 45px; top: 448px; width: 170px; text-align: center; font-family: "Oswald", sans-serif; font-weight: 600; font-size: 26px; letter-spacing: -0.3px; color: var(--ink); }
  .price-box {
    left: 45px; top: 482px; width: 170px; height: 72px;
    background: var(--gold); border-radius: 2px;
    text-align: center; font-family: "Oswald", sans-serif; font-weight: 600; color: var(--ink);
  }
  .price { display: block; font-size: 40px; line-height: 46px; margin-top: 4px; letter-spacing: -0.5px; }
  .price-note { display: block; font-size: 15px; line-height: 16px; }
  .accessory {
    width: 112px; height: 112px; border-radius: 50%;
    border: 3px solid var(--teal); background: #fff;
    display: flex; align-items: center; justify-content: center;
  }
  .accessory--mic { left: 249px; top: 460px; }
  .accessory--receiver { left: 375px; top: 460px; }
  .shot--mic {
    width: 62px; height: 62px; border-radius: 50%;
    background: radial-gradient(circle at 50% 45%, #fff 0 38%, #2b2b2b 42%, #3a3a3a 52%, var(--accent-orange) 58%, #fff 66%);
  }
  .shot--receiver {
    width: 70px; height: 56px; border-radius: 4px;
    background: linear-gradient(180deg, #fff 0 35%, #3a3a3d 40%, #161618 100%);
  }
  .accessory-caption { width: 130px; text-align: center; color: var(--teal); font-size: 10px; font-weight: 600; line-height: 1.25; }
  .caption--mic { left: 240px; top: 581px; }
  .caption--receiver { left: 366px; top: 581px; }
  .offices { left: 0; top: 641px; width: 540px; display: flex; justify-content: center; gap: 14px; font-size: 8.5px; }
  .offices li { list-style: none; }
  .offices li::before { content: "•"; margin-right: 7px; }
  .sheet-title { position: absolute; top: 803px; left: 0; width: 1200px; text-align: center; font-family: "Raleway", sans-serif; font-size: 24px; color: #333; letter-spacing: 0.5px; }
</style>
</head>
<body>

<section class="page page--plain">
  <svg class="decor" viewBox="0 0 540 698" aria-hidden="true">
    <polygon points="0,0 205,0 205,88 150,88 0,52" fill="var(--shape-soft)"/>
    <polygon points="205,0 330,0 255,88 205,88" fill="var(--shape)"/>
    <polygon points="330,0 430,0 400,40 300,40" fill="var(--shape-soft)"/>
    <polygon points="380,440 540,520 540,698 300,698 380,600" fill="var(--shape-soft)"/>
    <polygon points="0,600 140,698 0,698" fill="var(--shape)"/>
  </svg>
  <div class="brand abs"><span class="brand-mark"></span><span class="brand-name">quorel signal works</span></div>
  <div class="tagline abs">AV fitness specials</div>
  <h1 class="headline abs">Complete Fitness Studio Audio Systems</h1>
  <p class="intro abs">Need to update your tired and unreliable audio system – Quorel Signal have a complete range of systems or can customise a package to suit your exact requirements.</p>
  <svg class="connectors" viewBox="0 0 540 698" aria-hidden="true" fill="none" stroke="var(--teal)" stroke-width="4">
    <polyline points="215,330 231,330 231,267 248,267"/>
    <polyline points="130,354 130,424 248,424"/>
    <line x1="215" y1="518" x2="250" y2="518"/>
    <line x1="305" y1="450" x2="305" y2="462"/>
    <line x1="431" y1="450" x2="431" y2="462"/>
  </svg>
  <div class="speaker speaker--left abs" role="img" aria-label="Photo of a black 10 inch speaker cabinet"></div>
  <div class="speaker speaker--right abs" role="img" aria-label="Photo of a black 10 inch speaker cabinet"></div>
  <div class="label label--speakers abs">2x Vantor 10”<br>250 watt speakers</div>
  <div class="product--amp abs" role="img" aria-label="Photo of a rack-mount 2 x 250 watt power amplifier"></div>
  <div class="label label--amp abs">2 x 250 watt amplifier<br>( 2 yr warranty)</div>
  <div class="product--player abs" role="img" aria-label="Photo of a rack-mount media player with jog wheel"></div>
  <div class="product--mixer abs" role="img" aria-label="Photo of a rack-mount fitness audio mixer"></div>
  <div class="label label--mixer abs">Fitness Series Audio mixer</div>
  <div class="offer-lead abs">All for just</div>
  <div class="price-box abs"><span class="price">$2740</span><span class="price-note">plus GST</span></div>
  <div class="accessory accessory--mic abs"><div class="shot--mic" role="img" aria-label="Photo of a black and orange fitness headset microphone"></div></div>
  <div class="accessory accessory--receiver abs"><div class="shot--receiver" role="img" aria-label="Photo of a wireless microphone receiver with antennas"></div></div>
  <p class="accessory-caption caption--mic abs">Professional fitness wireless microphone system</p>
  <p class="accessory-caption caption--receiver abs">Fitness instructors wireless headmic</p>
  <ul class="offices abs"><li>Melbourne</li><li>Brisbane</li><li>Sydney</li><li>Perth</li></ul>
</section>

<section class="page page--photo">
  <svg class="decor" viewBox="0 0 540 698" aria-hidden="true">
    <polygon points="0,0 205,0 205,88 150,88 0,52" fill="var(--shape-soft)"/>
    <polygon points="205,0 330,0 255,88 205,88" fill="var(--shape)"/>
    <polygon points="330,0 430,0 400,40 300,40" fill="var(--shape-soft)"/>
  </svg>
  <div class="backdrop-photo abs" role="img" aria-label="Faded photo of a woman exercising on gym equipment"></div>
  <div class="brand abs"><span class="brand-mark"></span><span class="brand-name">quorel signal works</span></div>
  <div class="tagline abs">AV fitness specials</div>
  <h1 class="headline abs">Complete Fitness Studio Audio Systems</h1>
  <p class="intro abs">Need to update your tired and unreliable audio system – Quorel Signal have a complete range of systems or can customise a package to suit your exact requirements.</p>
  <svg class="connectors" viewBox="0 0 540 698" aria-hidden="true" fill="none" stroke="var(--teal)" stroke-width="4">
    <polyline points="215,330 231,330 231,267 248,267"/>
    <polyline points="130,354 130,424 248,424"/>
    <line x1="215" y1="518" x2="250" y2="518"/>
    <line x1="305" y1="450" x2="305" y2="462"/>
    <line x1="431" y1="450" x2="431" y2="462"/>
  </svg>
  <div class="speaker speaker--left abs" role="img" aria-label="Photo of a black 10 inch speaker cabinet"></div>
  <div class="speaker speaker--right abs" role="img" aria-label="Photo of a black 10 inch speaker cabinet"></div>
  <div class="label label--speakers abs">2x Vantor 10”<br>250 watt speakers</div>
  <div class="product--amp abs" role="img" aria-label="Photo of a rack-mount 2 x 250 watt power amplifier"></div>
  <div class="label label--amp abs">2 x 250 watt amplifier<br>( 2 yr warranty)</div>
  <div class="product--player abs" role="img" aria-label="Photo of a rack-mount media player with jog wheel"></div>
  <div class="product--mixer abs" role="img" aria-label="Photo of a rack-mount fitness audio mixer"></div>
  <div class="label label--mixer abs">Fitness Series Audio mixer</div>
  <div class="offer-lead abs">All for just</div>
  <div class="price-box abs"><span class="price">$2740</span><span class="price-note">plus GST</span></div>
  <div class="accessory accessory--mic abs"><div class="shot--mic" role="img" aria-label="Photo of a black and orange fitness headset microphone"></div></div>
  <div class="accessory accessory--receiver abs"><div class="shot--receiver" role="img" aria-label="Photo of a wireless microphone receiver with antennas"></div></div>
  <p class="accessory-caption caption--mic abs">Professional fitness wireless microphone system</p>
  <p class="accessory-caption caption--receiver abs">Fitness instructors wireless headmic</p>
  <ul class="offices abs"><li>Melbourne</li><li>Brisbane</li><li>Sydney</li><li>Perth</li></ul>
</section>

<p class="sheet-title">Third Page Options</p>

</body>
</html>
```